Investment company needing business card

We are wanting a business card which looks sharp and easy on the eye. We are thinking of having a business card with the logo embossed on it, to really make it stand out. We will only have a small amount of information of the business card, person's name, position, email address and phone number

Contact Information for Business Card

Danica Pruett
Executive Assistant
+64 21 547 3162
danicap@harwellcapital.co.nz

Requirements
Must have
• Embossed logo
Should not have
• Not to be busy

```html
<!DOCTYPE html>
<html lang="en">
<head>
<meta charset="utf-8">
<title>Harwell Capital business card options</title>
<link href="https://fonts.googleapis.com/css2?family=Open+Sans:wght@300;400;600;700&display=swap" rel="stylesheet">
<style>
:root{
  --board:#b0804e;
  --green:#34b073;
  --charcoal:#444142;
  --grey:#5f5f5f;
  --light:#f4f4f4;
  --white:#ffffff;
  --ink:#111111;
}
*{box-sizing:border-box;margin:0;padding:0}
html,body{width:1200px;height:1157px;overflow:hidden}
body{background:var(--board);font-family:"Open Sans",sans-serif;position:relative}
.option-title{position:absolute;width:454px;text-align:center;color:var(--white);font-weight:700;font-size:22px;line-height:1}
.card{position:absolute;width:454px;height:259px;overflow:hidden;box-shadow:2px 3px 5px rgba(0,0,0,.35)}
.card > *{position:absolute}
.rounded{border-radius:16px}
.center{left:0;width:100%;text-align:center}
.brand{display:flex;align-items:center;gap:8px;font-weight:700;font-size:21px;letter-spacing:.5px;color:var(--green);white-space:nowrap;line-height:1}
.brand .mark{width:26px;height:26px;background:var(--green);display:block}
.brand.centered{left:0;width:100%;justify-content:center}
.name{font-weight:600;font-size:17px;color:var(--green);line-height:1;white-space:nowrap}
.role{font-weight:300;font-size:12.5px;color:var(--grey);line-height:1;white-space:nowrap}
.contact{font-size:12.5px;line-height:1;white-space:nowrap;letter-spacing:.3px}
.label{font-weight:600;color:var(--green)}
.big-square{background:var(--grey)}
/* option 1 */
.card-dark{background:#000}
.card-dark .role{color:#8a8a8a}
/* option 2 */
.card-rule{background:var(--white)}
.card-rule .divider{left:225px;top:76px;width:2px;height:96px;background:#cfcfcf}
.card-rule .band{left:0;bottom:0;width:100%;height:32px;background:var(--green)}
.card-rule .contact{color:#9a9a9a;display:flex;align-items:center;gap:6px}
.card-rule .small{font-size:10.5px;color:#b8b8b8}
/* option 4 */
.card-split{background:var(--light)}
.card-split .dark-half{left:0;top:0;width:204px;height:100%;background:linear-gradient(90deg,#111 0%,#333 100%)}
.card-split .contact{color:var(--white)}
/* option 6 */
.card-arc{background:var(--white)}
.card-arc .brand{color:var(--white)}
.card-arc .brand .mark{background:var(--white)}
.card-arc .rule{left:30px;top:209px;width:395px;height:1px;background:var(--green)}
</style>
</head>
<body>

<!-- Option 1 -->
<div class="option-title" style="left:92px;top:59px">Option 1</div>
<section class="card card-dark" style="left:92px;top:96px">
  <div class="brand centered" style="top:56px"><span class="mark"></span>HARWELL CAPITAL</div>
  <div class="name center" style="top:129px">Danica Pruett</div>
  <div class="role center" style="top:150px">Executive Assistant</div>
  <div class="contact center" style="top:209px;color:var(--green)"><span class="label">Phone:</span> +64 21 547 3162</div>
  <div class="contact center" style="top:228px;color:var(--white);font-size:14px;letter-spacing:.8px">danicap@harwellcapital.co.nz</div>
</section>

<!-- Option 2 -->
<div class="option-title" style="left:624px;top:59px">Option 2</div>
<section class="card card-rule rounded" style="left:624px;top:116px;height:260px">
  <div class="brand" style="left:16px;top:110px;font-size:17px"><span class="mark" style="width:22px;height:22px"></span>HARWELL CAPITAL</div>
  <div class="divider"></div>
  <div class="name" style="left:241px;top:91px">Danica Pruett</div>
  <div class="role" style="left:241px;top:111px">Executive Assistant</div>
  <div class="contact" style="left:240px;top:136px">
    <svg width="9" height="9" viewBox="0 0 10 10" aria-hidden="true"><path d="M1 3c0-2 8-2 8 0v1H7V3H3v1H1z M2 5h6l1 4H1z" fill="var(--green)"/></svg>+64 21 547 3162</div>
  <div class="contact small" style="left:240px;top:158px;display:flex;align-items:center;gap:6px">
    <svg width="9" height="7" viewBox="0 0 10 8" aria-hidden="true"><rect x=".5" y=".5" width="9" height="7" fill="none" stroke="var(--green)"/><path d="M.5 .5 5 4.5 9.5 .5" fill="none" stroke="var(--green)"/></svg>danicap@harwellcapital.co.nz</div>
  <div class="band"></div>
</section>

<!-- Option 3 -->
<div class="option-title" style="left:98px;top:416px">Option 3</div>
<section class="card rounded" style="left:98px;top:450px;background:var(--white);border-radius:14px">
  <div class="brand" style="left:23px;top:41px"><span class="mark"></span>HARWELL CAPITAL</div>
  <div class="name" style="left:23px;top:141px">Danica Pruett</div>
  <div class="role" style="left:23px;top:160px">Executive Assistant</div>
  <div class="big-square" style="left:330px;top:140px;width:77px;height:69px"></div>
  <svg style="left:0;top:227px" width="454" height="32" viewBox="0 0 454 32" aria-hidden="true">
    <rect width="454" height="32" fill="var(--charcoal)"/>
    <path d="M0 0H282L302 32H0Z" fill="var(--green)"/>
  </svg>
  <div class="contact" style="left:23px;top:236px;color:var(--white);font-size:14px;letter-spacing:.8px">danicap@harwellcapital.co.nz</div>
</section>

<!-- Option 4 -->
<div class="option-title" style="left:620px;top:416px">Option 4</div>
<section class="card card-split rounded" style="left:620px;top:450px">
  <div class="dark-half"></div>
  <div class="big-square" style="left:54px;top:66px;width:100px;height:90px"></div>
  <div class="contact" style="left:0;width:204px;text-align:center;top:209px"><span class="label">Phone:</span> +64 21 547 3162</div>
  <div class="contact" style="left:0;width:204px;text-align:center;top:228px;font-size:11.5px">danicap@harwellcapital.co.nz</div>
  <div class="brand" style="left:204px;width:250px;justify-content:center;top:100px;font-size:17px"><span class="mark" style="width:22px;height:22px"></span>HARWELL CAPITAL</div>
  <div class="name" style="left:204px;width:250px;text-align:center;top:212px">Danica Pruett</div>
  <div class="role" style="left:204px;width:250px;text-align:center;top:231px">Executive Assistant</div>
</section>

<!-- Option 5 -->
<div class="option-title" style="left:98px;top:753px">Option 5</div>
<section class="card" style="left:98px;top:790px;background:var(--white)">
  <div class="brand centered" style="top:33px"><span class="mark"></span>HARWELL CAPITAL</div>
  <div class="name center" style="top:104px;font-size:19px">Danica Pruett</div>
  <div class="role center" style="top:128px;font-size:13.5px">Executive Assistant</div>
  <svg style="left:0;top:186px" width="454" height="57" viewBox="0 0 454 57" aria-hidden="true">
    <path d="M188 20H454V57H170Z" fill="var(--grey)"/>
    <path d="M0 0H225L198 37H0Z" fill="var(--green)"/>
  </svg>
  <div class="contact" style="left:21px;top:198px;color:var(--white);font-weight:600;font-size:13.5px;letter-spacing:0">Phone: +64 21 547 3162</div>
  <div class="contact" style="left:218px;top:217px;color:var(--white);letter-spacing:.6px">danicap@harwellcapital.co.nz</div>
</section>

<!-- Option 6 -->
<div class="option-title" style="left:612px;top:753px">Option 6</div>
<section class="card card-arc" style="left:612px;top:790px;width:455px;height:261px">
  <svg style="left:0;top:0" width="455" height="130" viewBox="0 0 455 130" aria-hidden="true">
    <path d="M0 85Q227 150 455 85V96Q227 160 0 96Z" fill="#ececec"/>
    <path d="M0 0H455V78Q227 142 0 78Z" fill="var(--green)"/>
  </svg>
  <div class="brand centered" style="top:52px"><span class="mark"></span>HARWELL CAPITAL</div>
  <div class="name center" style="top:147px;font-size:19px">Danica Pruett</div>
  <div class="role center" style="top:172px;font-size:13px;color:#444">Executive Assistant</div>
  <div class="rule"></div>
  <div class="contact center" style="top:218px;color:var(--grey);letter-spacing:0"><span class="label">Phone:</span> +64 21 547 3162,&nbsp; <span class="label">Email:</span> danicap@harwellcapital.co.nz</div>
</section>

</body>
</html>
```